Letterhead and business card design

We have recently had a logo designed by brightnook. now we need a corporate identity with business card and lettehead design.

Target Market(s)

law firms corporates

Industry/Entity Type

Business

Requirements
Should not have
• cheesy detecive stuff like magnifying glasses etxcc

```html
<!DOCTYPE html>
<html lang="en">
<head>
<meta charset="utf-8">
<title>Halvorsen &amp; Reid – Letterhead and Fax</title>
<link href="https://fonts.googleapis.com/css2?family=Questrial&family=Arimo:wght@400;700&display=swap" rel="stylesheet">
<style>
  :root {
    --backdrop: #ebebeb;
    --paper: #f8f8f7;
    --ink: #3a3a3a;
    --ink-soft: #666;
    --ink-faint: #8a8a8a;
    --rule: #9a9a9a;
    --band: #b4b4b4;
    --signature: #d7deef;
  }
  * { margin: 0; padding: 0; box-sizing: border-box; }
  html, body { width: 1200px; height: 815px; overflow: hidden; }
  body { background: var(--backdrop); position: relative; font-family: "Questrial", sans-serif; color: var(--ink); }

  .sheet { position: absolute; top: 70px; width: 481px; height: 683px; background: var(--paper); }
  .sheet--letter { left: 80px; }
  .sheet--fax { left: 638px; }

  .brand { position: absolute; text-align: center; color: var(--ink-soft); }
  .brand__name { font-family: "Questrial", sans-serif; font-size: 22px; line-height: 1; }
  .brand__tagline { font-family: "Questrial", sans-serif; font-size: 10px; line-height: 1; margin-top: 6px; }
  .sheet--letter .brand { left: 120px; top: 52px; width: 240px; }
  .sheet--fax .brand { left: 222px; top: 52px; width: 240px; }

  .letter { position: absolute; left: 35px; top: 190px; width: 413px; font-size: 7.8px; line-height: 12px; }
  .letter__greeting { font-family: "Arimo", sans-serif; font-weight: 700; font-size: 7.5px; margin-bottom: 9px; }
  .letter p { text-align: justify; margin-bottom: 12px; }

  .signoff { position: absolute; right: 33px; top: 492px; text-align: right; font-size: 7.5px; line-height: 11px; color: var(--ink); }
  .signoff strong { font-family: "Arimo", sans-serif; font-weight: 700; margin-left: 3px; }
  .signoff__name { margin-top: 13px; }
  .signature { position: absolute; left: 265px; top: 520px; width: 112px; height: 24px; background: linear-gradient(90deg, var(--signature), #e8ecf6); border-radius: 12px; }

  .footer { position: absolute; left: 30px; width: 421px; top: 616px; text-align: center; font-size: 6.2px; color: var(--ink-soft); }
  .footer__address { line-height: 8px; }
  .footer__contact { line-height: 8px; }
  .footer__contact b { font-family: "Arimo", sans-serif; font-weight: 700; }
  .footer__rule { height: 1px; background: var(--rule); margin: 6px 0 4px; }
  .footer__legal { font-size: 5.2px; line-height: 6.5px; color: var(--ink-faint); padding: 0 40px; }
  .sheet__band { position: absolute; left: 0; right: 0; bottom: 0; height: 10px; background: var(--band); }

  .fax-title { position: absolute; left: 20px; top: 36px; font-family: "Arimo", sans-serif; font-size: 56px; line-height: 1; color: var(--ink-soft); letter-spacing: 1px; }

  .fax-details { position: absolute; left: 24px; top: 143px; width: 436px; border-collapse: collapse; font-family: "Arimo", sans-serif; font-size: 6.5px; font-weight: 700; color: var(--ink); }
  .fax-details td { border: 1px solid var(--rule); height: 14.3px; padding: 0 3px; }
  .fax-details .label { width: 46px; }
  .fax-details .value { width: 172px; }

  .fax-message { position: absolute; left: 22px; top: 229px; width: 438px; height: 361px; border: 1px solid var(--rule); font-family: "Arimo", sans-serif; }
  .fax-flags { display: flex; height: 17px; border-bottom: 1px solid var(--rule); background: #efefef; font-size: 6.8px; font-weight: 700; }
  .fax-flags span { flex: 1; display: flex; align-items: center; justify-content: center; gap: 4px; border-right: 1px solid var(--rule); }
  .fax-flags span:last-child { border-right: none; }
  .fax-flags i { width: 5px; height: 5px; border: 1px solid var(--ink-soft); }
  .fax-message__label { text-align: center; font-size: 6.8px; margin-top: 10px; color: var(--ink); }
</style>
</head>
<body>

<section class="sheet sheet--letter">
  <div class="brand">
    <div class="brand__name">Halvorsen &amp; Reid</div>
    <div class="brand__tagline">Investigations · Security · Intelligence</div>
  </div>

  <div class="letter">
    <div class="letter__greeting">Dear sir / madame,</div>
    <p>Lorem ipsum dolor sit amet, consectetur adipisicing elit, sed do eiusmod tempor incididunt ut labore et dolore magna aliqua. Ut enim ad minim veniam, quis nostrud exercitation ullamco laboris nisi ut aliquip ex ea commodo consequat. Duis aute irure dolor in reprehenderit in voluptate velit esse cillum dolore eu fugiat nulla pariatur. Excepteur sint occaecat cupidatat non proident, sunt in culpa qui officia deserunt mollit anim id est laborum.Lorem ipsum dolor sit amet, consectetur adipisicing elit, sed do eiusmod tempor incididunt ut labore et dolore magna aliqua. Ut enim ad minim veniam, quis nostrud exercitation ullamco laboris nisi ut aliquip ex ea commodo consequat. Duis aute irure dolor in reprehenderit in voluptate velit esse cillum dolore eu fugiat nulla pariatur. Excepteur sint occaecat cupidatat non proident, sunt in culpa qui officia deserunt mollit anim id est laborum.</p>
    <p>Lorem ipsum dolor sit amet, consectetur adipisicing elit, sed do eiusmod tempor incididunt ut labore et dolore magna aliqua. Ut enim ad minim veniam, quis nostrud exercitation ullamco laboris nisi ut aliquip ex ea commodo consequat. Duis aute irure dolor in reprehenderit in voluptate velit esse cillum dolore eu fugiat nulla pariatur. Excepteur sint occaecat cupidatat non proident, sunt in culpa qui officia deserunt mollit anim id est laborum.</p>
    <p>Lorem ipsum dolor sit amet, consectetur adipisicing elit, sed do eiusmod tempor incididunt ut labore et dolore magna aliqua. Ut enim ad minim veniam, quis nostrud exercitation ullamco laboris nisi ut aliquip ex ea commodo consequat. Duis aute irure dolor in reprehenderit in voluptate velit esse cillum dolore eu fugiat nulla pariatur. Excepteur sint occaecat cupidatat non proident, sunt in culpa qui officia deserunt mollit anim id est laborum.</p>
  </div>

  <div class="signoff">
    <div>Yours faithfully <strong>HALVORSEN AND REID</strong></div>
    <div class="signoff__name">Marcus Reid</div>
    <div>Director</div>
  </div>
  <div class="signature" role="img" aria-label="Handwritten signature of the director"></div>

  <footer class="footer">
    <div class="footer__address">PO Box 118, Harbour Lane, Auckland, New Zealand</div>
    <div class="footer__contact"><b>Tel:</b> +64 9 555 0142 &nbsp;• <b>Fax:</b> +64 9 555 0187 &nbsp;• <b>Email:</b> marcus@halvorsenreid.co.nz &nbsp;• www.halvorsenreid.co.nz</div>
    <div class="footer__rule"></div>
    <div class="footer__legal">Government Licenced Private Investigators (licence number 480256). Halvorsen and Reid Investigations Limited have no more authority than that of an ordinary private citizen to require a reply to this correspondence.</div>
  </footer>
  <div class="sheet__band"></div>
</section>

<section class="sheet sheet--fax">
  <div class="fax-title">FAX</div>
  <div class="brand">
    <div class="brand__name">Halvorsen &amp; Reid</div>
    <div class="brand__tagline">Investigations · Security · Intelligence</div>
  </div>

  <table class="fax-details">
    <tr><td class="label">To:</td><td class="value"></td><td class="label">From:</td><td class="value"></td></tr>
    <tr><td class="label">Fax:</td><td class="value"></td><td class="label">Pages:</td><td class="value"></td></tr>
    <tr><td class="label">Phone:</td><td class="value"></td><td class="label">Date:</td><td class="value"></td></tr>
    <tr><td class="label">Re:</td><td class="value"></td><td class="label">CC:</td><td class="value"></td></tr>
  </table>

  <div class="fax-message">
    <div class="fax-flags">
      <span><i></i>Urgent</span>
      <span><i></i>For Review</span>
      <span><i></i>Please Comment</span>
      <span><i></i>Please Reply</span>
      <span><i></i>Confidential</span>
    </div>
    <div class="fax-message__label">COMMENTS:</div>
  </div>

  <footer class="footer">
    <div class="footer__address">PO Box 118, Harbour Lane, Auckland, New Zealand</div>
    <div class="footer__contact"><b>Tel:</b> +64 9 555 0142 &nbsp;• <b>Fax:</b> +64 9 555 0187 &nbsp;• <b>Email:</b> marcus@halvorsenreid.co.nz &nbsp;• www.halvorsenreid.co.nz</div>
    <div class="footer__rule"></div>
    <div class="footer__legal">Government Licenced Private Investigators (licence number 480256). Halvorsen and Reid Investigations Limited have no more authority than that of an ordinary private citizen to require a reply to this correspondence.</div>
  </footer>
  <div class="sheet__band"></div>
</section>

</body>
</html>
```